Design a website for our "Bright Stride" Initiative we are implementing at our Youth Soccer Club.

We need a web design for a wellness initiative for our soccer club. "Bright Stride" is the program title. The website will have health and wellness content related to our initiative. It should have interactive features for our users. Videos, survey/data submission capabilities, etc. Colors themed to align with logo. see my start of a website at www.brightstridewithtown.com. I like the homepage design, the rest is unprofessional looking. Design should provide education, tips, advice, resources, for health & wellness; wellness related to our pillars. 6 tabs in addition to home page: Drink more water, fuel your performance, stretch more, protect your skin more, move more, and sports mindset. (year 2 diagram wheel). Sports counseling will be next big focus. Wordpress based website. Easy for me to update in the future.

Target Market(s)

Families with children participating in soccer. concept also applicable to other youth sports.

Industry/Entity Type

Health And Wellness

Number of Pages Required

5+ page

Font styles to use
Sans Serif

Colors
0292cd
f37122

Requirements
Must have
• Bright Stride Logo
• Marrowdale Soccer Club Logo (*updated*)
• Home page
• Video included that is currently on the website homepage www.brightstridewithtown.com
• Page for each of the 6 pillars
• Focus on "drink more water" pillar and "Mindset" (will focus on sports counseling)
• Flexibility for me to update/edit the website moving forward (non-coding).
• User friendly graphic/picture interface
Nice to have
• Design focused more on the themes, not on soccer. Want the design to be applicable to parents and youth of all sports. Education and interactive features to all ages.

```html
<!DOCTYPE html>
<html lang="en">
<head>
<meta charset="utf-8">
<title>Bright Stride – Health &amp; Wellness</title>
<link rel="stylesheet" href="https://fonts.googleapis.com/css2?family=Open+Sans:wght@400;600;700&family=Montserrat:wght@500;600&display=swap">
<style>
:root{
  --blue:#0292cd;
  --blue-light:#41b6e8;
  --blue-nav:rgba(84,178,222,.88);
  --orange:#f37122;
  --orange-light:#f6944c;
  --teal:#0e7f8c;
  --text:#333;
  --muted:#8a8a8a;
  --grey-bg:#f4f4f4;
  --white:#fff;
}
*{box-sizing:border-box;margin:0;padding:0}
html,body{width:1200px;height:3191px;overflow:hidden}
body{font-family:"Open Sans",Arial,sans-serif;color:var(--text);background:var(--white);position:relative}
.abs{position:absolute}
/* header */
.site-header{position:absolute;left:0;top:0;width:1200px;height:118px;background:var(--white)}
.brand{position:absolute;left:133px;top:40px;display:flex;align-items:center;gap:12px}
.brand-dot{width:34px;height:34px;border-radius:50%;background:var(--orange)}
.brand-name{font-weight:700;font-size:26px;letter-spacing:1.5px;color:var(--teal)}
.search{position:absolute;left:818px;top:60px;width:252px;height:35px;border:1px solid #ccc;border-radius:18px;font-size:11px;color:#999;padding:10px 18px}
.search svg{position:absolute;right:12px;top:9px}
/* hero */
.hero{position:absolute;left:0;top:118px;width:1200px;height:554px;background:linear-gradient(120deg,#d9d4cc 0%,#b9b2a8 40%,#7d7a78 75%,#5b5a5c 100%)}
.main-nav{position:absolute;left:0;top:0;width:1200px;height:52px;background:var(--blue-nav);display:flex;padding-left:132px}
.main-nav a{color:var(--white);font-weight:600;font-size:16.5px;text-decoration:none;line-height:52px;padding:0 9px;border-right:1px solid rgba(255,255,255,.45)}
.main-nav a:last-child{border-right:0}
.hero-title{position:absolute;left:133px;top:222px;font-family:"Montserrat",Arial,sans-serif;font-weight:500;color:var(--white);font-size:37px;line-height:46px;letter-spacing:1px}
.btn-outline{position:absolute;border:2px solid var(--white);color:var(--white);font-size:13px;font-weight:600;text-align:center}
.hero .btn-outline{left:133px;top:329px;width:157px;height:43px;line-height:39px;font-size:15px}
.dots{position:absolute;left:548px;top:509px;display:flex;gap:8px}
.dots span{width:14px;height:14px;border-radius:50%;border:2px solid var(--white)}
.dots span.on{background:var(--white)}
/* welcome */
.welcome{position:absolute;left:0;top:672px;width:1200px;height:420px}
.welcome h1{position:absolute;left:140px;top:70px;font-weight:400;font-size:34px;color:#333}
.welcome p{position:absolute;left:142px;width:430px;font-size:14px;line-height:26px;color:var(--muted)}
.btn-orange{position:absolute;background:var(--orange);color:var(--white);font-size:13px;font-weight:600;text-align:center}
.welcome .btn-orange{left:142px;top:298px;width:136px;height:36px;line-height:36px}
.video-frame{position:absolute;left:615px;top:66px;width:455px;height:288px;background:linear-gradient(135deg,#5f8a3e,#9cbf6c 50%,#d8cfc1)}
.play{position:absolute;left:50%;top:50%;width:78px;height:78px;margin:-39px 0 0 -39px;border:3px solid var(--white);border-radius:50%}
.play::after{content:"";position:absolute;left:30px;top:22px;border-left:24px solid var(--white);border-top:15px solid transparent;border-bottom:15px solid transparent}
.play.sm{width:56px;height:56px;margin:-28px 0 0 -28px}
.play.sm::after{left:21px;top:15px;border-left:18px solid var(--white);border-top:11px solid transparent;border-bottom:11px solid transparent}
/* pillars band */
.pillars{position:absolute;left:0;top:1092px;width:1200px;height:476px;background:linear-gradient(180deg,#42b6e7,#2a8dd0)}
.pillar-photo{position:absolute;width:303px;height:182px}
.pillar-panel{position:absolute;width:303px;height:182px;background:rgba(255,255,255,.18);color:var(--white);text-align:center}
.pillar-panel h3{font-weight:400;font-size:20px;margin-top:20px}
.pillar-panel p{font-size:11.5px;line-height:16px;padding:6px 28px 0}
.pillar-panel .btn-outline{position:relative;display:inline-block;margin-top:12px;width:110px;height:30px;line-height:26px;font-size:11px;border-width:1.5px}
/* diagram */
.wheel{position:absolute;left:0;top:1568px;width:1200px;height:500px;background:var(--grey-bg)}
.wheel h2{position:absolute;left:0;top:36px;width:1200px;text-align:center;font-weight:600;font-size:24px;color:#444;letter-spacing:.5px}
.wheel-label{position:absolute;font-size:14px;line-height:16px;color:#333;text-transform:uppercase;white-space:nowrap}
.wheel-label.right{text-align:left}
.wheel-label.left{text-align:right}
.wheel-name{position:absolute;left:500px;top:410px;width:200px;text-align:center;font-weight:700;font-size:22px;color:var(--teal)}
/* survey */
.survey{position:absolute;left:0;top:2068px;width:1200px;height:362px}
.section-title{position:absolute;left:133px;font-weight:400;font-size:29px;color:#333}
.survey-photo{position:absolute;width:188px;height:188px;border-radius:50%}
.survey-item h4{position:absolute;font-size:16px;font-weight:600;color:var(--blue)}
.survey-item p{position:absolute;width:250px;font-size:12.5px;line-height:20px;color:var(--muted)}
.survey-item .more{position:absolute;font-size:12.5px;font-weight:700;color:var(--orange)}
/* videos */
.videos{position:absolute;left:0;top:2430px;width:1200px;height:392px;background:var(--grey-bg)}
.video-thumb{position:absolute;top:100px;width:305px;height:197px}
/* footer */
.site-footer{position:absolute;left:0;top:2822px;width:1200px;height:369px;background:linear-gradient(180deg,var(--orange-light),#ee5a12);color:var(--white)}
.footer-col{position:absolute;top:56px}
.footer-col h5{font-weight:400;font-size:17px;margin-bottom:8px;letter-spacing:.3px}
.footer-col li{list-style:none;font-size:14.5px;line-height:27px}
.social{display:flex;gap:6px;margin-top:4px}
.social span{width:36px;height:36px;border:2px solid var(--white);border-radius:50%}
.footer-rule{position:absolute;left:140px;top:295px;width:940px;height:1px;background:rgba(255,255,255,.4)}
.copyright{position:absolute;left:0;top:320px;width:1200px;text-align:center;font-size:11.5px;opacity:.9}
</style>
</head>
<body>

<header class="site-header">
  <div class="brand"><span class="brand-dot"></span><span class="brand-name">BRIGHT STRIDE</span></div>
  <div class="search">Search here
    <svg width="16" height="16" viewBox="0 0 16 16"><circle cx="6.5" cy="6.5" r="5" fill="none" stroke="#888" stroke-width="1.8"/><line x1="10.3" y1="10.3" x2="15" y2="15" stroke="#888" stroke-width="2"/></svg>
  </div>
</header>

<section class="hero" role="img" aria-label="Photo of a trainer coaching a woman doing lunges with dumbbells in a bright gym">
  <nav class="main-nav">
    <a>Drink more water</a><a>Fuel your performance</a><a>Stretch more</a><a>Protect your skin more</a><a>Move more</a><a>Sports Mindset</a>
  </nav>
  <div class="hero-title">HEALTH &amp; WELLNESS TIPS<br>FOR SOCCER CLUB</div>
  <div class="btn-outline">LEARN MORE</div>
  <div class="dots"><span class="on"></span><span class="on"></span><span class="on"></span><span></span></div>
</section>

<section class="welcome">
  <h1>Welcome to Bright Stride</h1>
  <p style="top:130px">Maecenas aliquet velit vel turpis Mauris neque metus malesuada nec ultricies sit amet porttitor mattis enim In massa libero interdum nec</p>
  <p style="top:220px">blandit sed nulla in ullamcorper est eget tempor cursus neque mi consectetuer mi a ultricies massa est sed nisl</p>
  <div class="btn-orange">READ MORE</div>
  <div class="video-frame" role="img" aria-label="Video still of a young man drinking from a water bottle on a basketball court"><span class="play"></span></div>
</section>

<section class="pillars">
  <div class="pillar-photo" style="left:130px;top:76px;background:linear-gradient(135deg,#6d7a86,#c2b8a8 60%,#8a5a44)" role="img" aria-label="Photo of soccer players drinking water on the sideline"></div>
  <div class="pillar-panel" style="left:130px;top:258px">
    <h3>Drink more Water</h3>
    <p>Maecenas aliquet velit vel turpis Mauris neque metus malesuada nec ultricies sit amet porttitor mattis enim</p>
    <span class="btn-outline">READ MORE</span>
  </div>
  <div class="pillar-panel" style="left:447px;top:76px">
    <h3>Mindset</h3>
    <p>Maecenas aliquet velit vel turpis Mauris neque metus malesuada nec ultricies sit amet porttitor mattis enim</p>
    <span class="btn-outline">READ MORE</span>
  </div>
  <div class="pillar-photo" style="left:447px;top:258px;background:linear-gradient(135deg,#3d6f9e,#8fb4cf 55%,#2d3f55)" role="img" aria-label="Photo of a man training on a rowing machine"></div>
  <div class="pillar-photo" style="left:765px;top:76px;background:linear-gradient(135deg,#d9d2c6,#9fc3d9 50%,#2e6fa8)" role="img" aria-label="Photo of two women reviewing a clipboard in a gym"></div>
  <div class="pillar-panel" style="left:765px;top:258px">
    <h3>Sports Counselling</h3>
    <p>Maecenas aliquet velit vel turpis Mauris neque metus malesuada nec ultricies sit amet porttitor mattis enim</p>
    <span class="btn-outline">READ MORE</span>
  </div>
</section>

<section class="wheel">
  <h2>HOW BRIGHT STRIDE IS</h2>
  <svg class="abs" style="left:0;top:0" width="1200" height="500" viewBox="0 0 1200 500">
    <path d="M390 500 A210 210 0 0 1 810 500" fill="none" stroke="var(--blue)" stroke-width="34"/>
    <g stroke="#9a9a9a" stroke-width="1.5">
      <line x1="498" y1="166" x2="536" y2="260"/>
      <line x1="694" y1="160" x2="666" y2="260"/>
      <line x1="351" y1="266" x2="432" y2="330"/>
      <line x1="845" y1="256" x2="770" y2="322"/>
      <line x1="279" y1="411" x2="380" y2="430"/>
      <line x1="921" y1="405" x2="822" y2="430"/>
    </g>
    <g fill="var(--white)" stroke="#888" stroke-width="1.5">
      <circle cx="536" cy="260" r="6"/><circle cx="666" cy="260" r="6"/>
      <circle cx="432" cy="330" r="6"/><circle cx="770" cy="322" r="6"/>
      <circle cx="380" cy="430" r="6"/><circle cx="822" cy="430" r="6"/>
    </g>
    <g fill="var(--orange)">
      <circle cx="498" cy="166" r="44"/><circle cx="694" cy="160" r="44"/>
      <circle cx="351" cy="266" r="44"/><circle cx="845" cy="256" r="44"/>
      <circle cx="279" cy="411" r="44"/><circle cx="921" cy="405" r="44"/>
    </g>
    <g fill="none" stroke="var(--white)" stroke-width="3" stroke-linecap="round" stroke-linejoin="round">
      <rect x="486" y="146" width="24" height="38" rx="4"/><rect x="490" y="138" width="16" height="8"/><path d="M498 158 q-5 8 0 12 q5 -4 0 -12z"/>
      <path d="M674 170 a20 20 0 1 1 40 0"/><line x1="694" y1="170" x2="704" y2="156"/><circle cx="694" cy="170" r="3"/>
      <path d="M336 250 h30 v12 a15 15 0 0 1 -30 0z"/><line x1="351" y1="277" x2="351" y2="284"/><line x1="340" y1="286" x2="362" y2="286"/>
      <path d="M826 270 h40 v-8 h-22 l-10 -18"/><circle cx="840" cy="240" r="4"/>
      <path d="M258 418 l8 -16 l12 6 q14 4 24 12 v6 h-44z"/>
      <path d="M899 405 a22 22 0 0 1 44 0z"/><path d="M921 405 v16 a5 5 0 0 1 -10 0"/>
    </g>
  </svg>
  <div class="wheel-label left" style="left:318px;top:134px;width:125px">Drink more<br>water</div>
  <div class="wheel-label right" style="left:746px;top:130px">Fuel<br>your body</div>
  <div class="wheel-label left" style="left:180px;top:242px;width:120px">Sports<br>mindset</div>
  <div class="wheel-label right" style="left:898px;top:238px">Stretch<br>more</div>
  <div class="wheel-label left" style="left:130px;top:390px;width:92px">Move<br>more</div>
  <div class="wheel-label right" style="left:975px;top:388px">Protect<br>your skin</div>
  <div class="wheel-name">Bright Stride</div>
</section>

<section class="survey">
  <h2 class="section-title" style="top:42px">Latest Health Survey</h2>
  <div class="survey-item">
    <div class="survey-photo" style="left:130px;top:105px;background:radial-gradient(circle,#c9c9c9,#7f8e73)" role="img" aria-label="Photo of a runner checking a fitness watch"></div>
    <h4 style="left:340px;top:118px">Performance and hydration</h4>
    <p style="left:340px;top:148px">Maecenas aliquet velit vel turpis Mauris neque metus malesuada nec ultricies sit amet porttitor mattis enim In massa libero interdum nec interdum v</p>
    <div class="more" style="left:340px;top:250px">READ MORE</div>
  </div>
  <div class="survey-item">
    <div class="survey-photo" style="left:615px;top:105px;background:radial-gradient(circle,#c94a5a,#5a3a2a)" role="img" aria-label="Photo of fresh fruit, dumbbells and a measuring tape on a table"></div>
    <h4 style="left:824px;top:118px">Boost performance</h4>
    <p style="left:824px;top:148px">Maecenas aliquet velit vel turpis Mauris neque metus malesuada nec ultricies sit amet porttitor mattis enim In massa libero interdum nec interdum v</p>
    <div class="more" style="left:824px;top:250px">READ MORE</div>
  </div>
</section>

<section class="videos">
  <h2 class="section-title" style="top:42px">Our Videos</h2>
  <div class="video-thumb" style="left:130px;background:linear-gradient(135deg,#2c3330,#56605a 50%,#1f2522)" role="img" aria-label="Video still of a soccer player kicking a ball in the rain"><span class="play sm"></span></div>
  <div class="video-thumb" style="left:447px;background:linear-gradient(135deg,#f2c66d,#e6e6e6 50%,#9b7fb8)" role="img" aria-label="Video still of a healthy breakfast bowl with fruit and dumbbells"><span class="play sm"></span></div>
  <div class="video-thumb" style="left:768px;background:linear-gradient(135deg,#6b5a55,#b68a7a 50%,#2b2a2e)" role="img" aria-label="Video still of an athlete doing pull-ups"><span class="play sm"></span></div>
</section>

<footer class="site-footer">
  <div class="footer-col" style="left:160px">
    <h5>COMPANY</h5>
    <ul><li>Drink more water</li><li>Fuel your performance</li><li>Stretch more</li><li>Protect your skin more</li></ul>
  </div>
  <div class="footer-col" style="left:382px">
    <h5>RESOURCES</h5>
    <ul><li>Move more</li><li>Sports mindset</li><li>Videos</li><li>Blogs</li></ul>
  </div>
  <div class="footer-col" style="left:571px">
    <h5>CONTACT INFO</h5>
    <ul><li>418 Alderbrook Lane Suite 12</li><li>Marrowdale, PA 10483</li><li>(555) 014-3827</li><li>hello@brightstride.example</li></ul>
  </div>
  <div class="footer-col" style="left:857px">
    <h5>FOLLOW US</h5>
    <div class="social"><span></span><span></span><span></span><span></span></div>
  </div>
  <div class="footer-rule"></div>
  <div class="copyright">© 2017 Bright Stride. All right reserved. Term of Use</div>
</footer>

</body>
</html>
```